African homeware retailer needs a web page design

We need a web page design for a new homeware and accessories store based in Johannesburg, South Africa. Our store carries modern African inspired items from designers that support social development and poverty alleviation initiatives. We have a particular preference for outfits that are centred on the empowerment of women.

Our business celebrates the skill, design and product of African craft and the work of designers looking to take that forward in a socially beneficial way (creating employment, developing skills, supporting local crafts people etc). We aim to carry items and inspirations from all over the African continent.

We would like to see a design that communicates African beauty and elegance without the typical tribal references that are made in reference to African craft or art.

We would like the web page to be stylish, uncomplicated, modern, captivating and appealing to the discerning customer. A similar value proposition is that of http://www.lanterwickhouse.example/.

This is an e-commerce website which must be attractive to both individual buyers and design professionals so the website needs to look professional.

Here are links to some websites we like:
http://www.corvellinteriors.example/
http://www.tmerrow.example/

Our logo is attached to the brief.

Target Market(s)

Our target market is female, age 20-50. However should not alienate the design conscious male customer therefore

Industry/Entity Type

E-Commerce

Requirements
Must have
• - A featured product banner which includes a photograph and text. This should be easy to edit as we will be changing the featured product regularly
- An easily expendable products section with categories. Examples of categories could be cushions, bedding, crockery etc. Should be easy to add new categories as well as new product pictures
- Home/landing page should be uncluttered
- Should use the logo and should be easy to change the logo which we have in various colour combinations. We plan to change the logo colours depending on circumstance e.g. make it red and white around Valentines day (similar to the way Quorbit frequently changes the logo on their landing page)

```html
<!DOCTYPE html>
<html lang="en">
<head>
<meta charset="utf-8">
<title>Savanna Lane – Homeware &amp; Accessories</title>
<link rel="stylesheet" href="https://fonts.googleapis.com/css2?family=Lato:wght@300;400;700&amp;family=Raleway:wght@400;500&amp;display=swap">
<style>
  :root {
    --green: #3a9b47;
    --green-band: #3f9a3f;
    --navy: #163c5a;
    --ink: #333;
    --muted: #8a8a8a;
    --soft: #9a9a9a;
    --line: #d6d6d6;
    --panel: #ececec;
    --white: #fff;
  }
  * { box-sizing: border-box; margin: 0; padding: 0; }
  html, body { width: 1200px; height: 907px; overflow: hidden; background: var(--white); }
  body { position: relative; font-family: "Lato", Arial, sans-serif; color: var(--ink); }
  a { color: inherit; text-decoration: none; }
  .abs { position: absolute; }

  .top-rule { left: 0; top: 0; width: 1200px; height: 3px; background: var(--green); }

  /* fixed sidebar */
  .sidebar { left: 0; top: 3px; width: 390px; height: 849px; border-left: 1px solid #e2e2e2; }
  .brand { left: 0; top: 36px; width: 568px; text-align: center; width: 390px; padding-left: 180px; }
  .brand-mark { display: block; width: 64px; height: 64px; border-radius: 50%; background: var(--green); margin: 0 auto 16px; }
  .brand-name { font-family: "Raleway", sans-serif; font-weight: 500; font-size: 22px; letter-spacing: 3px; color: var(--green); }
  .side-nav { left: 184px; top: 228px; width: 200px; list-style: none; text-align: center; }
  .side-nav li { height: 36.8px; font-size: 12.5px; color: var(--muted); }
  .side-nav li.active { color: var(--green); font-weight: 700; }

  .note-line { left: 183px; width: 1px; background: #b5b5b5; }
  .note-tick { left: 170px; width: 28px; height: 1px; background: #b5b5b5; }
  .note-text { left: 184px; top: 248px; transform: translate(-50%, -50%) rotate(-90deg); white-space: nowrap; font-family: Arial, sans-serif; font-size: 12px; color: #999; }

  /* header */
  .search { left: 400px; top: 10px; width: 366px; height: 30px; border: 1px solid #cfcfcf; font-size: 9px; color: var(--muted); padding: 10px 11px; }
  .search svg { position: absolute; right: 8px; top: 6px; }
  .account { left: 783px; top: 19px; font-size: 9.5px; color: var(--navy); }
  .account span { color: var(--muted); margin: 0 5px; }
  .cart { left: 884px; top: 12px; width: 138px; height: 27px; border: 1px solid #cfcfcf; font-size: 10.5px; color: var(--navy); }
  .cart svg { position: absolute; left: 7px; top: 4px; }
  .cart .count { position: absolute; left: 34px; top: 7px; color: var(--soft); }
  .cart .checkout { position: absolute; left: 62px; top: 7px; }

  .stage { left: 390px; top: 48px; width: 810px; height: 598px; background: var(--panel); }
  .main-nav { left: 390px; top: 48px; width: 632px; height: 39px; background: var(--white); display: flex; justify-content: center; align-items: center; font-size: 11.5px; letter-spacing: .3px; color: #2b2b2b; }
  .main-nav .sep { margin: 0 18px; }

  .hero { left: 400px; top: 87px; width: 619px; height: 227px; background: linear-gradient(135deg, #dfe9c9 0%, #b9d86a 45%, #e4ecd8 100%); }
  .dot { top: 284px; width: 14px; height: 14px; border-radius: 50%; border: 1.5px solid #fff; }
  .dot.on { background: var(--navy); }
  .hero-bar { left: 400px; top: 313px; width: 622px; height: 65px; background: var(--white); }
  .hero-title { left: 424px; top: 324px; font-family: "Raleway", sans-serif; font-size: 37px; letter-spacing: 1.5px; color: var(--navy); }
  .shop-now { font-size: 12px; color: #555; }
  .shop-now::after { content: ""; display: inline-block; margin-left: 6px; border-left: 5px solid #666; border-top: 3.5px solid transparent; border-bottom: 3.5px solid transparent; vertical-align: 1px; }
  .hero-shop { left: 906px; top: 337px; font-size: 16px; color: #666; }

  .section-title { left: 404px; top: 391px; font-size: 16px; color: var(--green); }
  .view-all { left: 913px; top: 397px; font-size: 10.5px; color: var(--muted); text-decoration: underline; }

  .card { top: 424px; width: 195px; }
  .card .photo { height: 162px; }
  .card .meta { margin-top: 14px; border-top: 1px solid var(--line); display: flex; justify-content: space-between; align-items: center; padding: 10px 0 0 2px; }
  .card .label { font-size: 14px; font-weight: 700; color: var(--green); }

  /* footer */
  .foot-col { list-style: none; font-size: 9.5px; color: var(--muted); }
  .foot-col li { height: 29px; }
  .news-title { left: 798px; top: 689px; font-size: 14px; color: var(--ink); }
  .news-input { left: 798px; top: 716px; width: 225px; height: 33px; border: 1px solid #cfcfcf; font-size: 10px; color: var(--soft); padding: 11px 10px; }
  .news-input svg { position: absolute; right: 10px; top: 9px; }
  .social { top: 765px; width: 18px; height: 18px; border-radius: 50%; background: #7a7a7a; }

  .legal { left: 0; top: 852px; width: 1200px; height: 55px; background: var(--green-band); }
  .copyright { left: 624px; top: 870px; font-size: 14px; font-weight: 300; color: #dcefd9; }
</style>
</head>
<body>
  <div class="abs top-rule"></div>

  <aside class="abs sidebar">
    <div class="abs brand">
      <span class="brand-mark"></span>
      <span class="brand-name">SAVANNA LANE</span>
    </div>
    <ul class="abs side-nav">
      <li class="active">HOME</li>
      <li>NEW ARRIVAL</li>
      <li>FEATURED</li>
      <li>HOMEWARE</li>
      <li>ACCESSORIES</li>
      <li>NEWS</li>
      <li>CONTACT US</li>
    </ul>
  </aside>

  <div class="abs note-tick" style="top:19px"></div>
  <div class="abs note-line" style="top:19px;height:148px"></div>
  <div class="abs note-line" style="top:325px;height:147px"></div>
  <div class="abs note-tick" style="top:472px"></div>
  <div class="abs note-text">No scrolling fixed area</div>

  <div class="abs stage"></div>

  <div class="abs search">SEARCH ENTIRE STORE HERE
    <svg width="16" height="16" viewBox="0 0 16 16"><circle cx="6.5" cy="6.5" r="4.8" fill="none" stroke="#3a9b47" stroke-width="2"/><line x1="10" y1="10" x2="14.5" y2="14.5" stroke="#3a9b47" stroke-width="2.5" stroke-linecap="round"/></svg>
  </div>
  <div class="abs account">LOG IN<span>|</span>SIGN UP</div>
  <div class="abs cart">
    <svg width="24" height="19" viewBox="0 0 24 19"><path d="M1 2h4l3 10h12l2-7H7" fill="none" stroke="#3a9b47" stroke-width="1.8"/><circle cx="10" cy="16" r="1.7" fill="#3a9b47"/><circle cx="18" cy="16" r="1.7" fill="#3a9b47"/></svg>
    <span class="count">(0)</span>
    <span class="checkout">CHECKOUT ▸</span>
  </div>

  <nav class="abs main-nav">
    <span>LIVING</span><span class="sep">|</span><span>BEDROOM</span><span class="sep">|</span><span>BATHROOM</span><span class="sep">|</span><span>KITCHEN</span><span class="sep">|</span><span>LIGHTING</span><span class="sep">|</span><span>ARTWORK &amp; DECOR</span>
  </nav>

  <div class="abs hero" role="img" aria-label="Featured product photo: green and white patterned ceramic cups and plates"></div>
  <span class="abs dot" style="left:947px"></span>
  <span class="abs dot on" style="left:969px"></span>
  <span class="abs dot" style="left:991px"></span>
  <div class="abs hero-bar"></div>
  <div class="abs hero-title">CROCKERY</div>
  <a class="abs shop-now hero-shop">SHOP NOW</a>

  <h2 class="abs section-title" style="font-weight:400">FEAUTURED PRODUCTS</h2>
  <a class="abs view-all">VIEW ALL PRODUCTS</a>

  <div class="abs card" style="left:402px">
    <div class="photo" role="img" aria-label="Grey hand-made ceramic jugs and cups" style="background:linear-gradient(135deg,#f2f2f0,#c9c8c4 60%,#e8e8e6)"></div>
    <div class="meta"><span class="label">CROCKERY</span><a class="shop-now">SHOP NOW</a></div>
  </div>
  <div class="abs card" style="left:615px">
    <div class="photo" role="img" aria-label="Woven pendant lamps glowing orange" style="background:radial-gradient(circle at 45% 80%,#ff5a1f,#d8782f 40%,#b9a27a 75%,#8a7a5a)"></div>
    <div class="meta"><span class="label">LIGHTING</span><a class="shop-now">SHOP NOW</a></div>
  </div>
  <div class="abs card" style="left:827px">
    <div class="photo" role="img" aria-label="Dark wooden candle lanterns" style="background:linear-gradient(90deg,#dfe4e8,#6b4a38 45%,#e4e6e8 70%,#4a3024)"></div>
    <div class="meta"><span class="label">ACCESSORIES</span><a class="shop-now">SHOP NOW</a></div>
  </div>

  <ul class="abs foot-col" style="left:416px;top:695px"><li>STORE LOCATOR</li><li>MY ACCOUNT</li><li>HELP</li><li>CONTACT US</li></ul>
  <ul class="abs foot-col" style="left:539px;top:699px"><li>ABOUT US</li><li>PRESS &amp; NEWS</li><li>CAREERS</li><li>SUSTAINABILITY</li></ul>
  <ul class="abs foot-col" style="left:662px;top:695px"><li>HELP</li><li>FAQ</li><li>TERMS &amp; CONDITIONS</li><li>DISCLAIMER</li></ul>

  <div class="abs news-title">NEWSLETTER</div>
  <div class="abs news-input">ENTER YOUR EMAIL
    <svg width="32" height="14" viewBox="0 0 32 14"><line x1="0" y1="2" x2="8" y2="2" stroke="#163c5a" stroke-width="1.2"/><line x1="3" y1="5" x2="8" y2="5" stroke="#163c5a" stroke-width="1.2"/><rect x="11" y="1" width="20" height="12" fill="none" stroke="#163c5a" stroke-width="1.6"/><path d="M11 1l10 7 10-7" fill="none" stroke="#163c5a" stroke-width="1.6"/></svg>
  </div>
  <span class="abs social" style="left:797px"></span>
  <span class="abs social" style="left:831px"></span>
  <span class="abs social" style="left:866px"></span>
  <span class="abs social" style="left:901px"></span>
  <span class="abs social" style="left:938px"></span>

  <footer class="abs legal"></footer>
  <div class="abs copyright">Copyright 2014 © Savanna Lane . All Rights Reserved</div>
</body>
</html>
```